Etiketten für Vodka
Zielgruppe
Herstellung und Abfüllung von Spirituosen
Zielgruppe für die Kubus Range sind Bars, Clubs, Feste/Festivals
Aufgabenstellung
Unsere Kubus-Range umfasst rund 40 Spirituosen und deckt nahezu alles ab, was in einer modernen und gut sortierten Theke nicht fehlen darf.
Zum Jahreswechsel möchten wir die gesamte Range relaunchen und suchen im ersten Schritt ein Vorder-, Rückenetikett und Halsschleife für den Hauptartikel Vodka, welches in nachfolgenden Schritten auf die anderen Artikel übertragen werden soll.
Das Design soll wertig sein, auf unsere eigene Herstellung von Destillaten und Kräuterauszügen hinweisen.
Bei dem bestehenden Design kann der Barkeeper die Sorten leicht unterscheiden, dies soll auch weiterhin so bleiben.
Das Logo 'Kubus' ist eine eingetragen Wort-Bild-Marke und muss im Vorderetikett bestehen bleiben.
Max Größe Vorderetikett: Höhe 150mm, Breite 60mm
Max Größe Rückenetikett: Höhe 100mm, Breite 40mm

```html
<!DOCTYPE html>
<html lang="de">
<head>
<meta charset="utf-8">
<title>Kubus Vodka – Halsschleife und Vorderetikett</title>
<link rel="stylesheet" href="https://fonts.googleapis.com/css2?family=Montserrat:wght@600;700&family=Noto+Sans:wght@700&display=swap">
<style>
  :root {
    --bg: #ebebec;
    --label-blue: #a2b4bd;
    --art-tone: #7f949e;
    --art-shade: #5f737c;
    --ink: #263238;
    --band-teal: #3e6a79;
    --plate-rim: #c4c6c8;
    --plate-black: #050505;
    --white: #ffffff;
  }
  * { margin: 0; padding: 0; box-sizing: border-box; }
  html, body { width: 1200px; height: 1200px; overflow: hidden; background: var(--bg); }
  .canvas { position: relative; width: 1200px; height: 1200px; }

  .neck-label { position: absolute; left: 300px; top: 40px; width: 600px; height: 230px; }
  .neck-label svg { display: block; width: 600px; height: 230px; }
  .neck-label .word {
    font-family: "Noto Sans", sans-serif; font-weight: 700; font-size: 50px; fill: var(--ink);
  }

  .front-label {
    position: absolute; left: 458px; top: 310px; width: 284px; height: 840px;
    background: var(--label-blue); border-radius: 4px;
  }
  .front-label .pattern { position: absolute; inset: 0; background: var(--label-blue); border-radius: 4px; }
  .front-label .bartender-art {
    position: absolute; left: 57px; top: 50px; width: 150px; height: 216px;
    background: linear-gradient(180deg, var(--art-tone), var(--art-shade));
    border-radius: 6px;
  }
  .front-label .rule {
    position: absolute; left: 28px; top: 270px; width: 227px; height: 4px; background: var(--white);
  }
  .front-label .claim {
    position: absolute; left: 0; top: 281px; width: 100%; text-align: center;
    font-family: "Montserrat", sans-serif; font-weight: 700; font-size: 19px; line-height: 24px;
    letter-spacing: 0.05em; color: var(--ink); white-space: nowrap;
  }
  .front-label .origin {
    position: absolute; left: 28px; top: 308px; width: 227px; height: 25px;
    background: var(--band-teal); color: var(--white);
    font-family: "Montserrat", sans-serif; font-weight: 700; font-size: 10px;
    letter-spacing: 0.34em; line-height: 25px; text-align: center; white-space: nowrap;
  }
  .brand-plate {
    position: absolute; left: -89px; top: 396px; width: 462px; height: 143px;
    background: var(--plate-rim); border-radius: 22px; padding: 10px;
  }
  .brand-plate .plate-inner {
    width: 100%; height: 100%; background: var(--plate-black); border-radius: 16px;
    display: flex; align-items: center; justify-content: center;
    font-family: "Montserrat", sans-serif; font-weight: 600; font-size: 84px;
    letter-spacing: 0.08em; color: var(--white); white-space: nowrap;
  }
  .front-label .variety {
    position: absolute; left: 0; top: 648px; width: 100%; text-align: center;
    font-family: "Noto Sans", sans-serif; font-weight: 700; font-size: 70px; line-height: 1;
    color: var(--ink); white-space: nowrap;
  }
</style>
</head>
<body>
<main class="canvas">

  <section class="neck-label" aria-label="Halsschleife">
    <svg viewBox="0 0 600 230" role="img" aria-label="Halsschleife mit wiederholtem S-Monogramm-Muster">
      <path d="M20 12 Q300 52 580 12 L600 170 Q300 240 0 170 Z" fill="var(--label-blue)"/>
      <text class="word" x="300" y="136" text-anchor="middle">vodka</text>
    </svg>
  </section>

  <section class="front-label" aria-label="Vorderetikett">
    <div class="pattern" role="img" aria-label="Wiederholtes S-Monogramm-Muster in Glitzerblau"></div>
    <div class="bartender-art" role="img" aria-label="Illustration eines Barkeepers beim Destillieren"></div>
    <div class="rule"></div>
    <p class="claim">PREMIUM DISTILLED</p>
    <p class="origin">MADE IN GERMANY</p>
    <div class="brand-plate">
      <div class="plate-inner">KUBUS</div>
    </div>
    <p class="variety">vodka</p>
  </section>

</main>
</body>
</html>
```